Flyer: helping to close the Global Digital Divide- V20 project.

We need a flyer designing for a nonprofit (www.brambleloop.org) based in Washington DC and London. We help to connect communities that have no internet so that they can get access to the health, educational, socio-economic benefits of internet connectivity. The project is ‘V20’ – internet for the Vital 20%.
The flyer will be sent to major corporations, governments, major universities, and the like.
The first half of the flyer will be design rich and incorporate the words (on the attached V20 document) in a creative and appealing way using design and color contrasts to highlight important points. The V20 Logo is attached also. I have also attached a similar but different PLRT document to give some ideas.
The second half of the flyer will be an MOU (Memorandum of Understanding) for the corporations to sign. This needs to be simple and look professional.
It is very important that we can change the words in the flyer once the design is complete without having to go back to the designer every time.

```html
<!DOCTYPE html>
<html lang="en">
<head>
<meta charset="utf-8">
<title>The V20 Charter – Digital Participation for the Vital 20%</title>
<link href="https://fonts.googleapis.com/css2?family=Roboto+Condensed:wght@400;500;700&display=swap" rel="stylesheet">
<style>
  :root{
    --page-bg:#ebe8e3;
    --white:#ffffff;
    --brand-blue:#1b6fb6;
    --deep-blue:#1f5fa8;
    --teal:#1a9c98;
    --teal-solid:#1fa39b;
    --navy-tile:#1d1f5e;
    --lime:#8dc63f;
    --ink:#1b2340;
    --heading-tab:#e4f3f5;
  }
  *{box-sizing:border-box;margin:0;padding:0}
  html,body{width:1200px;height:861px;overflow:hidden;background:var(--page-bg)}
  body{font-family:"Roboto Condensed",Arial,sans-serif;position:relative}

  .flyer{position:absolute;top:35px;width:550px;height:784px;overflow:hidden;
    background:linear-gradient(180deg,#1d6fb0 0%,#1e8aaa 22%,#1a9c98 45%,#1e8ea6 58%,#2c3592 72%,#2c3592 74%);
    box-shadow:0 4px 12px rgba(0,0,0,.25)}
  .flyer--left{left:32px}
  .flyer--right{left:617px}

  .header{position:absolute;left:0;top:0;width:550px;height:94px}
  .header-bg{position:absolute;inset:0}
  .brand-name{position:absolute;left:33px;top:29px;font-size:31px;font-weight:700;color:var(--brand-blue);letter-spacing:.3px;white-space:nowrap}
  .header-title{position:absolute;left:325px;top:28px;color:var(--white);font-weight:500;font-size:23px;line-height:27px;white-space:nowrap}
  .header-title span{display:block;padding-left:6px}

  .tab{position:absolute;top:127px;height:23px;background:var(--heading-tab);color:var(--deep-blue);font-weight:500;font-size:15px;line-height:23px;text-align:center}
  .tab--what{left:0;width:240px}
  .tab--why{left:307px;width:243px}

  .panel{position:absolute}
  .panel--what{left:0;top:150px;width:280px;height:355px;background:rgba(60,175,185,.35)}
  .panel--why{left:307px;top:150px;width:243px;height:259px;background:var(--teal-solid)}

  .body-text{position:absolute;font-size:8.3px;line-height:10px;color:var(--ink);text-align:justify}
  .body-text b{font-weight:700}
  .left-col{left:13px;width:249px}
  .left-col.intro{top:163px;text-align:left}
  .left-col.challenge{top:193px}
  .left-col.about{top:413px}
  .right-col{left:331px;width:191px;color:var(--white)}
  .right-col.lead{top:180px;font-weight:700}
  .right-col.live{top:230px}
  .right-col.needs{top:290px}
  .right-col.ecosystem{top:350px}

  .mission{position:absolute;left:7px;top:256px;width:266px;height:146px;background:rgba(40,170,160,.6)}
  .mission-intro{position:absolute;left:0;top:4px;width:266px;text-align:center;font-size:10.2px;line-height:12.5px;color:var(--white)}
  .mission-intro b,.mission-close b{color:var(--navy-tile);font-weight:700}
  .tiles{position:absolute;left:2px;top:32px;display:flex;gap:7px}
  .tile{width:81px;height:70px;background:var(--navy-tile);border-radius:9px;color:var(--white);text-align:center;font-weight:700;font-size:9.6px;line-height:10px;padding-top:8px}
  .tile-icon{display:block;margin:0 auto 6px;width:30px;height:30px}
  .mission-close{position:absolute;left:0;top:110px;width:266px;text-align:center;font-size:10px;line-height:12px;color:var(--white)}

  .join-bar{position:absolute;left:0;top:484px;width:280px;height:14px;background:var(--lime);color:var(--white);font-weight:500;font-size:10.5px;line-height:14px;text-align:center}
  .contact{position:absolute;left:22px;font-size:11px;color:var(--white);font-weight:500;display:flex;align-items:center;white-space:nowrap}
  .contact .label{display:inline-block;width:74px;text-align:right;margin-right:6px}
  .contact svg{margin-right:6px}
  .contact--mail{top:511px}
  .contact--web{top:535px}

  .white-strip{position:absolute;left:0;top:574px;width:550px;height:9px;background:var(--white)}
  .photo{position:absolute;left:0;top:583px;width:550px;height:201px}
  .photo--elder{background:linear-gradient(90deg,#5d6a3a 0%,#8b8a5a 40%,#a69a7a 60%,#6c6a4a 100%)}
  .photo--children{background:linear-gradient(90deg,#7a4a6a 0%,#c43a3a 40%,#b9825a 60%,#4a6aa8 85%,#8a6a4a 100%)}
  .copyright{position:absolute;font-size:7.8px;font-weight:700;color:var(--white);white-space:nowrap}
  .copyright--left{left:208px;top:765px}
  .copyright--right{left:22px;top:757px}

  .ring{position:absolute;left:335px;top:410px;width:410px;height:410px;border-radius:50%;background:var(--white)}
  .ring-core{position:absolute;left:23px;top:23px;width:364px;height:364px;border-radius:50%;background:var(--teal)}
</style>
</head>
<body>

<section class="flyer flyer--left">
  <header class="header">
    <svg class="header-bg" width="550" height="94" viewBox="0 0 550 94">
      <defs><linearGradient id="hdrA" x1="0" y1="0" x2="1" y2="0"><stop offset="0" stop-color="#1e5fae"/><stop offset="1" stop-color="#1d7cb5"/></linearGradient></defs>
      <rect width="550" height="94" fill="url(#hdrA)"/>
      <polygon points="0,0 328,0 297,94 0,94" fill="#fff"/>
    </svg>
    <div class="brand-name">The V20 Charter</div>
    <h1 class="header-title">Digital Participation<span>for the Vital 20%</span></h1>
  </header>

  <div class="panel panel--what"></div>
  <div class="panel panel--why"></div>
  <h2 class="tab tab--what">What is the V20 Charter?</h2>
  <h2 class="tab tab--why">Why support the V20 Charter?</h2>

  <p class="body-text left-col intro">The V20 Charter is about ensuring Digital Participation for the ‘Vital 20%’ wherever they may be in the world</p>
  <p class="body-text left-col challenge">More than 3 billion people remain unconnected, in many cases despite having access to internet. The number is disproportionately <b>poor, rural, illiterate</b> and <b>female</b>. The major challenges are cost, lack of digital skills and appropriate technology and applications relevant to local needs.</p>

  <div class="mission">
    <p class="mission-intro"><b>The V20 mission</b> is to accelerate digital adoption and community enrichment through</p>
    <div class="tiles">
      <div class="tile"><svg class="tile-icon" viewBox="0 0 30 30"><rect x="4" y="4" width="9" height="9" rx="2" fill="#fff"/><rect x="17" y="4" width="9" height="9" rx="2" fill="#8dc63f"/><rect x="4" y="17" width="9" height="9" rx="2" fill="#fff"/><rect x="17" y="17" width="9" height="9" rx="2" fill="#fff"/></svg>innovative<br>applications</div>
      <div class="tile"><svg class="tile-icon" viewBox="0 0 30 30"><path d="M3 12a17 17 0 0 1 24 0" fill="none" stroke="#fff" stroke-width="2.5" stroke-linecap="round"/><path d="M8 17a10 10 0 0 1 14 0" fill="none" stroke="#fff" stroke-width="2.5" stroke-linecap="round"/><circle cx="15" cy="23" r="3" fill="#8dc63f"/></svg>network<br>design</div>
      <div class="tile"><svg class="tile-icon" viewBox="0 0 30 30"><rect x="5" y="16" width="5" height="10" fill="#fff"/><rect x="12.5" y="10" width="5" height="16" fill="#fff"/><rect x="20" y="4" width="5" height="22" fill="#8dc63f"/></svg>business<br>models</div>
    </div>
    <p class="mission-close">to enable the next <b>3.9 billion people</b> to <b>participate in<br>the digital world</b></p>
  </div>

  <p class="body-text left-col about">V20 is a project driven, action led, collaboration between cross-industry global organisations, NGOs, Academic institutions and public and private sector entities seeking to enrich communities through implementing real world digital solutions.</p>

  <p class="body-text right-col lead">There is a collective moral imperative to invest in each person’s capacity for growth and opportunity, access to affordable digital content, applications, and services at adequate speed is critical.</p>
  <p class="body-text right-col live">V20 already has live ‘Digital Participation’ projects in the field designed to enable communities to access the educational, health, social and financial benefits that flow from affordable and sustainable digital inclusion.</p>
  <p class="body-text right-col needs">V20 meets the needs of organizations and their staff to help address global Digital Equity through contributing projects, diverse skills, software and hardware technologies and solutions, community engagement and funding to real world projects.</p>
  <p class="body-text right-col ecosystem">V20 and its ecosystem of partners will curate projects and help assemble partnerships, skills and funding to meet the needs of the community.</p>

  <div class="join-bar">To join the V20 movement:</div>
  <div class="contact contact--mail"><span class="label">Contact us at:</span><svg width="18" height="13" viewBox="0 0 18 13"><rect x="1" y="1" width="16" height="11" fill="none" stroke="#8dc63f" stroke-width="1.5"/><polyline points="1,1 9,8 17,1" fill="none" stroke="#8dc63f" stroke-width="1.5"/></svg>partners@vitaltwenty.org</div>
  <div class="contact contact--web"><span class="label">Visit us at:</span><svg width="18" height="16" viewBox="0 0 18 16"><circle cx="8" cy="8" r="6.5" fill="none" stroke="#8dc63f" stroke-width="1.5"/><line x1="1.5" y1="8" x2="14.5" y2="8" stroke="#8dc63f" stroke-width="1.2"/><ellipse cx="8" cy="8" rx="3" ry="6.5" fill="none" stroke="#8dc63f" stroke-width="1.2"/></svg>www.vitaltwenty.org</div>

  <div class="white-strip"></div>
  <div class="photo photo--elder" role="img" aria-label="Photograph: a young boy with a laptop sitting beside an elderly woman outdoors in a rural village"></div>
  <div class="ring"><div class="ring-core"></div></div>
  <p class="copyright copyright--left">© 2021 The V20 Project www.vitaltwenty.org</p>
</section>

<section class="flyer flyer--right">
  <header class="header">
    <svg class="header-bg" width="550" height="94" viewBox="0 0 550 94">
      <defs><linearGradient id="hdrB" x1="0" y1="0" x2="1" y2="0"><stop offset="0" stop-color="#1e5fae"/><stop offset="1" stop-color="#1d7cb5"/></linearGradient></defs>
      <rect width="550" height="94" fill="url(#hdrB)"/>
      <polygon points="0,0 328,0 297,94 0,94" fill="#fff"/>
    </svg>
    <div class="brand-name">The V20 Charter</div>
    <h1 class="header-title">Digital Participation<span>for the Vital 20%</span></h1>
  </header>

  <div class="panel panel--what"></div>
  <div class="panel panel--why"></div>
  <h2 class="tab tab--what">What is the V20 Charter?</h2>
  <h2 class="tab tab--why">Why support the V20 Charter?</h2>

  <p class="body-text left-col intro">The V20 Charter is about ensuring Digital Participation for the ‘Vital 20%’ wherever they may be in the world</p>
  <p class="body-text left-col challenge">More than 3 billion people remain unconnected, in many cases despite having access to internet. The number is disproportionately <b>poor, rural, illiterate</b> and <b>female</b>. The major challenges are cost, lack of digital skills and appropriate technology and applications relevant to local needs.</p>

  <div class="mission">
    <p class="mission-intro"><b>The V20 mission</b> is to accelerate digital adoption and community enrichment through</p>
    <div class="tiles">
      <div class="tile"><svg class="tile-icon" viewBox="0 0 30 30"><rect x="4" y="4" width="9" height="9" rx="2" fill="#fff"/><rect x="17" y="4" width="9" height="9" rx="2" fill="#8dc63f"/><rect x="4" y="17" width="9" height="9" rx="2" fill="#fff"/><rect x="17" y="17" width="9" height="9" rx="2" fill="#fff"/></svg>innovative<br>applications</div>
      <div class="tile"><svg class="tile-icon" viewBox="0 0 30 30"><path d="M3 12a17 17 0 0 1 24 0" fill="none" stroke="#fff" stroke-width="2.5" stroke-linecap="round"/><path d="M8 17a10 10 0 0 1 14 0" fill="none" stroke="#fff" stroke-width="2.5" stroke-linecap="round"/><circle cx="15" cy="23" r="3" fill="#8dc63f"/></svg>network<br>design</div>
      <div class="tile"><svg class="tile-icon" viewBox="0 0 30 30"><rect x="5" y="16" width="5" height="10" fill="#fff"/><rect x="12.5" y="10" width="5" height="16" fill="#fff"/><rect x="20" y="4" width="5" height="22" fill="#8dc63f"/></svg>business<br>models</div>
    </div>
    <p class="mission-close">to enable the next <b>3.9 billion people</b> to <b>participate in<br>the digital world</b></p>
  </div>

  <p class="body-text left-col about">V20 is a project driven, action led, collaboration between cross-industry global organisations, NGOs, Academic institutions and public and private sector entities seeking to enrich communities through implementing real world digital solutions.</p>

  <p class="body-text right-col lead">There is a collective moral imperative to invest in each person’s capacity for growth and opportunity, access to affordable digital content, applications, and services at adequate speed is critical.</p>
  <p class="body-text right-col live">V20 already has live ‘Digital Participation’ projects in the field designed to enable communities to access the educational, health, social and financial benefits that flow from affordable and sustainable digital inclusion.</p>
  <p class="body-text right-col needs">V20 meets the needs of organizations and their staff to help address global Digital Equity through contributing projects, diverse skills, software and hardware technologies and solutions, community engagement and funding to real world projects.</p>
  <p class="body-text right-col ecosystem">V20 and its ecosystem of partners will curate projects and help assemble partnerships, skills and funding to meet the needs of the community.</p>

  <div class="join-bar">To join the V20 movement:</div>
  <div class="contact contact--mail"><span class="label">Contact us at:</span><svg width="18" height="13" viewBox="0 0 18 13"><rect x="1" y="1" width="16" height="11" fill="none" stroke="#8dc63f" stroke-width="1.5"/><polyline points="1,1 9,8 17,1" fill="none" stroke="#8dc63f" stroke-width="1.5"/></svg>partners@vitaltwenty.org</div>
  <div class="contact contact--web"><span class="label">Visit us at:</span><svg width="18" height="16" viewBox="0 0 18 16"><circle cx="8" cy="8" r="6.5" fill="none" stroke="#8dc63f" stroke-width="1.5"/><line x1="1.5" y1="8" x2="14.5" y2="8" stroke="#8dc63f" stroke-width="1.2"/><ellipse cx="8" cy="8" rx="3" ry="6.5" fill="none" stroke="#8dc63f" stroke-width="1.2"/></svg>www.vitaltwenty.org</div>

  <div class="white-strip"></div>
  <div class="photo photo--children" role="img" aria-label="Photograph: three smiling village children in bright clothes sitting together around a laptop"></div>
  <div class="ring"><div class="ring-core"></div></div>
  <p class="copyright copyright--right">© 2021 The V20 Project www.vitaltwenty.org</p>
</section>

</body>
</html>
```